Promo Flyer to put in prize bags at carnival

I am owner of Copper & Lark Hair Salon located in Brenmoor, OH. I’m sponsoring a community carnival when I will be putting flyers in all attendees prize bags. This flyer will communicate details of my salon on one side (picture of me, logo, description of business, address, website, email, phone #) and the other side will showcase and a 50% discount for first time customers. Flyer can be 5” x 7” or greater

Side 1 details:
-Logo will be attached to this brief
-picture of me will be attached to this brief
-address: 2561 W. Pellward Ave, Suite 17, Brenmoor, OH, 45871
-website: clhairstudio.example
-email: Dorian.welby@clhairstudio.example
-phone: 614-52-BOOKS (26657)

Side 2 details:
-‘Guess what? You get 50% off your 1st service at Copper & Lark Hair Salon.’
-‘Expires 7/31/2018’
-Hair | Fashion | Photography
-Visit clhairstudio.example to book your service
-must present this flyer at time of service to receive discount

Hair And Beauty

Other font styles liked:
• Inoxida

Colors
3176b5
000000
ffffff

Must have
• 2 sides
• Color scheme to match logo

```html
<!DOCTYPE html>
<html lang="en">
<head>
<meta charset="utf-8">
<title>Copper &amp; Lark Hair Salon – Promo Flyer</title>
<link href="https://fonts.googleapis.com/css2?family=Bitter:ital,wght@0,400;0,600;0,700;1,700&display=swap" rel="stylesheet">
<style>
  :root {
    --sky: #2fb2e6;
    --sky-deep: #1990cf;
    --sky-pale: #d6f1fc;
    --brand-blue: #3176b5;
    --gold: #f2a81d;
    --ink: #111111;
    --paper: #ffffff;
    --stage: #e9ebee;
    --photo-dark: #2b3a44;
    --photo-mid: #6d7f88;
  }
  * { box-sizing: border-box; margin: 0; padding: 0; }
  html, body { width: 1200px; height: 900px; overflow: hidden; }
  body {
    background: var(--stage);
    font-family: "Bitter", Georgia, serif;
    color: var(--ink);
    position: relative;
  }
  .flyer {
    position: absolute;
    top: 142px;
    width: 440px;
    height: 616px;
    overflow: hidden;
    background: var(--sky);
    box-shadow: 0 10px 30px rgba(0,0,0,.18);
  }
  .flyer--front { left: 120px; }
  .flyer--back { left: 640px; }
  .flyer__art { position: absolute; inset: 0; width: 100%; height: 100%; }

  /* Front */
  .brand-name {
    position: absolute;
    font-weight: 700;
    color: var(--brand-blue);
    white-space: nowrap;
  }
  .flyer--front .brand-name {
    left: 170px; top: 238px; width: 250px; text-align: center; font-size: 30px;
  }
  .contact-list {
    position: absolute; left: 140px; top: 298px; width: 296px;
    list-style: none; display: flex; flex-direction: column; align-items: center; gap: 10px;
  }
  .contact-item { display: flex; flex-direction: column; align-items: center; gap: 6px; }
  .contact-icon {
    width: 20px; height: 20px; border-radius: 50%;
    background: var(--paper); display: flex; align-items: center; justify-content: center;
  }
  .contact-icon svg { width: 12px; height: 12px; }
  .contact-bar {
    background: var(--gold); color: var(--ink);
    font-size: 11px; font-weight: 600; padding: 3px 8px; white-space: nowrap;
  }

  /* Back */
  .flyer--back .brand-name { left: 262px; top: 32px; width: 170px; text-align: center; font-size: 22px; }
  .offer-headline {
    position: absolute; left: 258px; top: 72px; width: 180px; text-align: center;
    font-style: italic; font-weight: 700; font-size: 22px; color: var(--brand-blue);
  }
  .offer-copy {
    position: absolute; left: 262px; top: 104px; width: 170px;
    font-size: 11px; font-weight: 600; line-height: 1.25;
  }
  .offer-badge {
    position: absolute; left: 236px; top: 146px; width: 128px; height: 128px; border-radius: 50%;
    background: var(--gold); border: 4px solid var(--paper);
    box-shadow: 0 0 0 3px var(--gold);
    display: flex; flex-direction: column; align-items: center; justify-content: center;
    color: var(--paper); text-align: center; line-height: 1;
  }
  .offer-badge__value { font-size: 36px; font-weight: 700; }
  .offer-badge__unit { font-size: 24px; font-weight: 700; }
  .offer-badge__note { font-size: 12px; font-weight: 600; margin-top: 4px; line-height: 1.1; }
  .service-photo {
    position: absolute; width: 104px; height: 104px; border-radius: 50%;
    border: 4px solid var(--gold);
    background: linear-gradient(145deg, var(--photo-mid), var(--photo-dark));
  }
  .service-photo--hair { left: -30px; top: 292px; background: linear-gradient(145deg, #8a6b58, #3a2e2a); }
  .service-photo--fashion { left: 168px; top: 300px; background: linear-gradient(145deg, #2f4d6b, #1b2430); }
  .service-photo--photography { left: 318px; top: 296px; background: linear-gradient(145deg, #c9d2d8, #4d5961); }
  .service-labels {
    position: absolute; left: 0; top: 408px; width: 440px; height: 24px;
    display: flex; background: rgba(255,255,255,.85);
  }
  .service-label { flex: 1; text-align: center; font-size: 12px; font-weight: 600; line-height: 24px; }
  .book-cta {
    position: absolute; left: 20px; top: 446px; width: 400px; height: 28px; border-radius: 14px;
    background: var(--gold); color: var(--paper); text-align: center;
    font-size: 14px; font-weight: 700; line-height: 28px; white-space: nowrap;
  }
  .book-cta__site { color: var(--ink); }
  .expiry {
    position: absolute; left: 120px; top: 484px; width: 200px; height: 24px;
    background: var(--paper); text-align: center; font-size: 14px; font-weight: 700; line-height: 24px;
  }
  .terms {
    position: absolute; left: 0; top: 514px; width: 440px; height: 24px;
    background: var(--paper); text-align: center; font-size: 11px; font-weight: 600; line-height: 24px;
  }
</style>
</head>
<body>

<section class="flyer flyer--front" aria-label="Flyer front: salon details">
  <svg class="flyer__art" viewBox="0 0 440 616" aria-hidden="true">
    <defs>
      <linearGradient id="front-sky" x1="0" y1="0" x2="0" y2="1">
        <stop offset="0" stop-color="#d6f1fc"/>
        <stop offset=".45" stop-color="#2fb2e6"/>
        <stop offset="1" stop-color="#1990cf"/>
      </linearGradient>
      <linearGradient id="front-photo" x1="0" y1="0" x2="1" y2="1">
        <stop offset="0" stop-color="#55646c"/>
        <stop offset=".5" stop-color="#2b3a44"/>
        <stop offset="1" stop-color="#1f5a6e"/>
      </linearGradient>
    </defs>
    <rect width="440" height="616" fill="url(#front-sky)"/>
    <g fill="#ffffff" opacity=".22">
      <circle cx="380" cy="150" r="26"/><circle cx="330" cy="420" r="18"/>
      <circle cx="60" cy="520" r="30"/><circle cx="200" cy="580" r="14"/>
      <circle cx="410" cy="540" r="22"/><circle cx="110" cy="440" r="12"/>
    </g>
    <path d="M0 490 C 140 560, 320 470, 440 520 V616 H0 Z" fill="#1990cf" opacity=".5"/>
    <path d="M0 380 C 70 370, 130 320, 170 250 C 210 170, 250 80, 330 0" fill="none" stroke="#ffffff" stroke-width="14" opacity=".8"/>
    <path d="M0 390 C 75 380, 138 328, 178 256 C 218 178, 262 86, 345 0" fill="none" stroke="#f2a81d" stroke-width="4"/>
  </svg>
  <svg class="flyer__art" viewBox="0 0 440 616" role="img" aria-label="Photo of the salon owner in a teal suit standing before a dark wooden doorway">
    <path d="M0 0 H318 C 246 80, 206 170, 166 246 C 126 320, 70 366, 0 374 Z" fill="url(#front-photo)"/>
  </svg>

  <p class="brand-name">Copper &amp; Lark</p>

  <ul class="contact-list">
    <li class="contact-item">
      <span class="contact-icon"><svg viewBox="0 0 12 12"><path d="M6 1a3.5 3.5 0 0 0-3.5 3.5C2.5 7 6 11 6 11s3.5-4 3.5-6.5A3.5 3.5 0 0 0 6 1z" fill="#3176b5"/><circle cx="6" cy="4.5" r="1.2" fill="#fff"/></svg></span>
      <span class="contact-bar">2561 W. Pellward Ave, Suite 17, Brenmoor, OH, 45871</span>
    </li>
    <li class="contact-item">
      <span class="contact-icon"><svg viewBox="0 0 12 12"><rect x="1" y="3" width="10" height="7" fill="none" stroke="#3176b5" stroke-width="1.2"/><path d="M1 3l5 4 5-4" fill="none" stroke="#3176b5" stroke-width="1.2"/></svg></span>
      <span class="contact-bar">Dorian.welby@clhairstudio.example</span>
    </li>
    <li class="contact-item">
      <span class="contact-icon"><svg viewBox="0 0 12 12"><path d="M3 1l2 2.5-1.2 1.3a7 7 0 0 0 3.4 3.4L8.5 7 11 9l-1.3 2C5.5 11 1 6.5 1 2.3z" fill="#3176b5"/></svg></span>
      <span class="contact-bar">(555) 52-BOOKS (555-522-6657)</span>
    </li>
    <li class="contact-item">
      <span class="contact-icon"><svg viewBox="0 0 12 12"><circle cx="6" cy="6" r="4.8" fill="none" stroke="#3176b5" stroke-width="1.1"/><path d="M1.2 6h9.6M6 1.2c-2 2.8-2 6.8 0 9.6M6 1.2c2 2.8 2 6.8 0 9.6" fill="none" stroke="#3176b5" stroke-width="1"/></svg></span>
      <span class="contact-bar">clhairstudio.example</span>
    </li>
  </ul>
</section>

<section class="flyer flyer--back" aria-label="Flyer back: first service discount">
  <svg class="flyer__art" viewBox="0 0 440 616" aria-hidden="true">
    <defs>
      <linearGradient id="back-sky" x1="0" y1="0" x2="0" y2="1">
        <stop offset="0" stop-color="#d6f1fc"/>
        <stop offset=".35" stop-color="#5cc4ee"/>
        <stop offset=".7" stop-color="#2fb2e6"/>
        <stop offset="1" stop-color="#1990cf"/>
      </linearGradient>
      <linearGradient id="back-photo" x1="0" y1="0" x2="1" y2="1">
        <stop offset="0" stop-color="#9a9a9a"/>
        <stop offset=".5" stop-color="#5a5a5a"/>
        <stop offset="1" stop-color="#cfcfcf"/>
      </linearGradient>
    </defs>
    <rect width="440" height="616" fill="url(#back-sky)"/>
    <g fill="#ffffff" opacity=".22">
      <circle cx="400" cy="250" r="20"/><circle cx="40" cy="580" r="26"/>
      <circle cx="300" cy="580" r="16"/><circle cx="140" cy="280" r="14"/>
    </g>
    <path d="M0 300 C 110 306, 220 280, 250 200 C 280 120, 260 40, 214 0" fill="none" stroke="#ffffff" stroke-width="12" opacity=".8"/>
    <path d="M0 310 C 118 316, 232 288, 262 204 C 292 122, 272 40, 226 0" fill="none" stroke="#f2a81d" stroke-width="4"/>
  </svg>
  <svg class="flyer__art" viewBox="0 0 440 616" role="img" aria-label="Black and white portrait of a model with short curly blonde hair">
    <path d="M0 0 H206 C 250 40, 268 120, 240 194 C 212 266, 110 294, 0 292 Z" fill="url(#back-photo)"/>
  </svg>

  <p class="brand-name">Copper &amp; Lark</p>
  <h1 class="offer-headline">Guess what?</h1>
  <p class="offer-copy">You get 50% off your 1st service at Copper &amp; Lark Hair Salon.</p>

  <div class="offer-badge">
    <span class="offer-badge__value">50%</span>
    <span class="offer-badge__unit">off</span>
    <span class="offer-badge__note">on your<br>1st service</span>
  </div>

  <div class="service-photo service-photo--hair" role="img" aria-label="Stylist working on a client's long brown hair"></div>
  <div class="service-photo service-photo--fashion" role="img" aria-label="Man in a navy suit being fitted by a tailor"></div>
  <div class="service-photo service-photo--photography" role="img" aria-label="Grid of men's haircut portrait shots"></div>

  <div class="service-labels">
    <span class="service-label">Hair</span>
    <span class="service-label">Fashion</span>
    <span class="service-label">Photography</span>
  </div>

  <p class="book-cta">Visit <span class="book-cta__site">clhairstudio.example</span> to book your service</p>
  <p class="expiry">Expires 7/31/2018</p>
  <p class="terms">must present this flyer at time of service to receive discount</p>
</section>

</body>
</html>
```